For Sale Sign for Real Estate Agency

We need a For Sale Sign designed for our agency. I want a very simple/elegant sign that says "For Sale" towards the top of the sign (not in huge letters). Most of the sign should be a design/picture with our name and phone number somewhere at the bottom.

One significant detail, it's important that our logo not be too big or the center piece of the sign. Since our company name has the word "rent" in it, people assume the house is for rent, instead of for sale.

I attached our logo and a rough outline of the format I'm looking for.

Again, I'm looking for elegant and simple! Thanks for your time

Industry/Entity Type

Real Estate

Colors

Designer to choose colors to be used in the design.

Requirements
Must have
Nice to have
Should not have
• Nothing tacky!
• Our logo/company name should not be too big or the center piece of the sign. Since our company name has the word "rent" in it, people assume the house is for rent, instead of for sale.

```html
<!DOCTYPE html>
<html lang="en">
<head>
<meta charset="utf-8">
<title>For Sale Sign</title>
<link rel="stylesheet" href="https://fonts.googleapis.com/css2?family=Anton&family=Montserrat:wght@400&family=Open+Sans:wght@700&display=swap">
<style>
  :root {
    --backdrop: #d6d7d9;
    --sign-white: #ffffff;
    --ink: #0b0b0b;
    --brand-red: #e52d24;
    --photo-dark: #2f2925;
    --photo-mid: #4d3e31;
    --photo-floor: #6b3f1c;
  }
  html, body {
    margin: 0;
    padding: 0;
    width: 900px;
    height: 1200px;
    overflow: hidden;
    background: var(--backdrop);
  }
  .canvas {
    position: relative;
    width: 900px;
    height: 1200px;
  }
  .sign {
    position: absolute;
    left: 143px;
    top: 162px;
    width: 640px;
    height: 906px;
    overflow: hidden;
    background: var(--sign-white);
  }
  .room-photo {
    position: absolute;
    left: 0;
    top: 140px;
    width: 640px;
    height: 680px;
    background: linear-gradient(180deg, var(--photo-dark) 0%, var(--photo-mid) 45%, var(--photo-floor) 80%, var(--photo-mid) 100%);
  }
  .sign-shapes {
    position: absolute;
    left: 0;
    top: 0;
    width: 640px;
    height: 906px;
  }
  .headline {
    position: absolute;
    left: 0;
    top: 38px;
    width: 640px;
    margin: 0;
    text-align: center;
    font-family: "Anton", "Oswald", sans-serif;
    font-weight: 400;
    font-size: 96px;
    line-height: 1.1;
    letter-spacing: 2px;
    color: var(--ink);
  }
  .agency-name {
    position: absolute;
    left: 0;
    top: 430px;
    width: 640px;
    margin: 0;
    display: flex;
    justify-content: center;
  }
  .agency-name .name-block {
    display: flex;
    flex-direction: column;
    align-items: flex-end;
    font-family: "Montserrat", sans-serif;
    font-weight: 400;
    color: var(--sign-white);
  }
  .agency-name .name-main {
    font-size: 54px;
    line-height: 1;
    letter-spacing: -1px;
  }
  .agency-name .name-sub {
    margin-top: 10px;
    font-size: 26px;
    line-height: 1;
    letter-spacing: 7px;
    margin-right: -7px;
  }
  .phone {
    position: absolute;
    left: 0;
    top: 790px;
    width: 640px;
    margin: 0;
    text-align: center;
    font-family: "Open Sans", sans-serif;
    font-weight: 700;
    font-size: 70px;
    line-height: 1.2;
    color: var(--sign-white);
  }
</style>
</head>
<body>
<div class="canvas">
  <div class="sign">
    <div class="room-photo" role="img" aria-label="Photo of an empty living room with hardwood floors, a brick fireplace and a doorway to the staircase"></div>
    <svg class="sign-shapes" viewBox="0 0 640 906" aria-hidden="true">
      <polygon points="0,0 640,0 640,156 320,298 0,153" fill="var(--sign-white)"/>
      <polygon points="336,300 640,156 640,178 352,300" fill="var(--brand-red)"/>
      <polygon points="0,796 320,652 602,778 602,790 320,664 0,808" fill="var(--sign-white)"/>
      <polygon points="0,808 320,664 640,806 640,906 0,906" fill="var(--brand-red)"/>
    </svg>
    <h1 class="headline">FOR SALE</h1>
    <p class="agency-name"><span class="name-block"><span class="name-main">Harbor Lane</span><span class="name-sub">Realty</span></span></p>
    <p class="phone">401.555.0148</p>
  </div>
</div>
</body>
</html>
```